Luxury Brand Coffee Table Book Template

Overview:
We are creating a premium, 28-page coffee table book to accompany every bespoke jewelry piece handcrafted by Vellmoor Jewelry. This book serves as an heirloom that documents the story, design, and craftsmanship behind each custom piece, culminating in a powerful legacy statement. We need a refined, luxurious, and masculine layout template that can be updated for each new customer.
**All reference files (images, logos, copy for pages, etc.) are included in the .zip file.
Deliverables:
Print-ready 28-page InDesign or editable template file
Front and back cover design
Consistent typography and page layouts based on our outlined structure
Design system that allows for easy photo and text updates per client
Specs:
Size: 8.1 x 10.6 in, Portrait Orientation
Cover: Black linen hardcover with gold foil stamped name or crest (simulated in mockup)
Interior: Deep matte photo paper feel – minimalistic, clean layout with generous whitespace
Color Palette: Black, white, and gold
Style: Bold, masculine, timeless, high-luxury (think Karvane Studio x Dellbrook & Co.)
See the attached 28-page outline. Please use stock image placeholders for now.
Target Market(s)
Affluent Men & Women age 35-65
Industry/Entity Type
Luxury Retail Jewelry
Font styles to use
Other font styles liked:
- I really like Trajan Pro 3, but open to suggestions, as well as a mixture of Serif and Sans Serif fonts
Look and feel
Each slider illustrates characteristics of the customer's brand and the style your logo design should communicate.

```html
<!DOCTYPE html>
<html lang="en">
<head>
<meta charset="utf-8">
<title>Vellmoor Jewelry — Coffee Table Book Template</title>
<link href="https://fonts.googleapis.com/css2?family=Cinzel:wght@500&family=EB+Garamond:wght@400&family=Italiana&display=swap" rel="stylesheet">
<style>
  :root {
    --backdrop: #d3d6d8;
    --ink: #0d0d0d;
    --charcoal: #2a2a2a;
    --paper: #f5f5f3;
    --white: #ffffff;
    --muted: #8a8a8a;
    --gold: #b8923e;
    --gold-deep: #8a6a2a;
    --gold-light: #d9bd6e;
    --rose: #b07a62;
    --sketch: #d9d9d7;
  }
  * { margin: 0; padding: 0; box-sizing: border-box; }
  html, body { width: 1200px; height: 2400px; overflow: hidden; }
  body { background: var(--backdrop); font-family: "EB Garamond", Georgia, serif; color: var(--ink); position: relative; }

  .panel { position: absolute; left: 0; width: 1200px; height: 800px; }
  .panel--cover { top: 0; }
  .panel--story { top: 800px; border-top: 1px solid #c6c9cb; }
  .panel--design { top: 1600px; border-top: 1px solid #c6c9cb; }

  /* Cover */
  .cover {
    position: absolute; left: 340px; top: 70px; width: 520px; height: 680px;
    background: var(--ink); display: flex; align-items: center; justify-content: center; gap: 14px;
  }
  .cover__mark { width: 38px; height: 38px; border-radius: 50%; background: var(--white); }
  .cover__name { font-family: "Cinzel", "Times New Roman", serif; font-weight: 500; color: var(--white); font-size: 22px; letter-spacing: 2px; }

  /* Spreads */
  .spread { position: absolute; left: 130px; top: 92px; width: 940px; height: 615px; display: flex; }
  .page { position: relative; width: 470px; height: 615px; overflow: hidden; }
  .page--dark { background: var(--ink); }
  .page--graphite { background: linear-gradient(160deg, #4a4a4a 0%, #2c2c2c 100%); }
  .page--light { background: var(--paper); }

  .photo { position: absolute; }
  .photo--ring-story { left: 40px; top: 110px; width: 390px; height: 380px;
    background: linear-gradient(165deg, var(--rose) 0%, #8d7a3a 45%, #3a3220 100%); }
  .photo--ring-design { left: 50px; top: 110px; width: 380px; height: 400px;
    background: linear-gradient(160deg, var(--gold-light) 0%, var(--gold) 50%, var(--gold-deep) 100%); }

  .folio { position: absolute; font-size: 10px; color: var(--muted); display: flex; align-items: center; gap: 6px; }
  .folio::after { content: ""; display: block; width: 26px; height: 1px; background: var(--muted); }
  .folio--left { left: 24px; bottom: 22px; flex-direction: row-reverse; }
  .folio--right { right: 10px; }

  .gutter-band { position: absolute; left: 0; top: 0; width: 34px; height: 100%; background: var(--ink); }

  .heading { font-family: "Italiana", "Times New Roman", serif; font-weight: 400; color: var(--ink); }
  .heading--story { position: absolute; left: 66px; top: 44px; font-size: 40px; }
  .heading--design { position: absolute; left: 40px; top: 70px; font-size: 34px; letter-spacing: 3px; }

  .body-copy { font-size: 8.5px; line-height: 1.45; color: #333; }
  .body-copy p + p { margin-top: 8px; }
  .story-intro { position: absolute; left: 66px; top: 100px; width: 360px; }
  .story-close { position: absolute; left: 190px; top: 450px; width: 250px; }

  .design-text { position: absolute; left: 40px; top: 126px; width: 170px; }
  .design-text p + p { margin-top: 12px; }
  .sketch { position: absolute; left: 250px; top: 30px; width: 100px; height: 110px; background: var(--sketch); }
  .eagle { position: absolute; left: 290px; top: 190px; width: 110px; height: 90px; background: var(--gold); }
  .feature-box { position: absolute; left: 250px; top: 360px; width: 170px; height: 170px; background: var(--ink); padding: 16px 14px; }
  .feature-box .body-copy { color: #e6e6e6; }
  .folio--story { top: 395px; }
  .folio--design { top: 330px; }
</style>
</head>
<body>

<section class="panel panel--cover">
  <div class="cover">
    <span class="cover__mark"></span>
    <span class="cover__name">Vellmoor Jewelry</span>
  </div>
</section>

<section class="panel panel--story">
  <div class="spread">
    <div class="page page--dark">
      <div class="photo photo--ring-story" role="img" aria-label="Photograph of a multi-tone gold signet ring with blue enamel crest and eagle shoulders on black"></div>
      <span class="folio folio--left">1</span>
    </div>
    <div class="page page--light">
      <div class="gutter-band"></div>
      <h2 class="heading heading--story">Story</h2>
      <div class="body-copy story-intro">
        <p>Every piece begins with a story worth keeping. We listen to the milestones, names and places that shaped the owner, and we carry them into metal.</p>
        <p>This chapter records how the idea first took shape and why it matters to the family that will wear it.</p>
      </div>
      <span class="folio folio--right folio--story">2</span>
      <div class="body-copy story-close">
        <p>Crafted by hand over many weeks, the ring holds the memory of a moment and the promise of the years to come. It is made to be passed on.</p>
      </div>
    </div>
  </div>
</section>

<section class="panel panel--design">
  <div class="spread">
    <div class="page page--graphite">
      <div class="photo photo--ring-design" role="img" aria-label="Photograph of a gold signet ring with eagle shoulder, rose gold crest and blue enamel"></div>
      <span class="folio folio--left">3</span>
    </div>
    <div class="page page--light">
      <h2 class="heading heading--design">DESIGN</h2>
      <div class="body-copy design-text">
        <p>The design opens with the owner's crest, drawn by hand and refined until each line carries meaning.</p>
        <p>Eagles guard both shoulders, a sign of strength and watchfulness.</p>
        <p>Rose, yellow and white gold meet in a single setting, each tone chosen for its place in the story.</p>
        <p>Blue enamel and fine engraving complete the face of the ring.</p>
      </div>
      <div class="sketch" role="img" aria-label="Pencil sketch of the crest with eagle and shield"></div>
      <div class="eagle" role="img" aria-label="Gold double-headed eagle emblem"></div>
      <span class="folio folio--right folio--design">4</span>
      <div class="feature-box">
        <div class="body-copy">
          <p>Sketches become wax, wax becomes gold. Every step is checked by the master jeweler before the next begins.</p>
          <p>The finished ring is signed inside the band.</p>
        </div>
      </div>
    </div>
  </div>
</section>

</body>
</html>
```